Web site for new fundraising service for charities

We need a web design for a new charitable trust based in New Zealand. With the economic downturn, charities are finding it increasingly difficult to raise the monies they need to deliver their services.

Using a network of fundraisers working out of their homes, BrightLot (our charitable trust) will source unique, high interest auction items on behalf of multiple charities - things like luxury cruises, exotic travel, luxury accommodation, fine dining, unique experiences with sports and entertainment personalities, tickets to sporting and entertainment events, etc.

Once we have sourced sufficient high value items we will then partner with Bidora (NZ's equivalent of Vendix) to launch the auction. The proceeds from each auction will benefit up to 6 charities. The auctions will be promoted through Bidora, through PR, and through the communications channels of the benefiting charities, reaching a wider audience than would be possible if just one charity was holding an auction and therefore resulting in more competitive bidding and higher returns for the charities.

We need a web site that we can point potential donors of auction items to, that gives them confidence in BrightLot. We will also leverage the web site with journalists. And of course, charities who are wondering whether or not to use BrightLot will come to our web site and check out our credentials. The tone of the site needs to be warm, friendly, approachable.

We are not locked into the blue and orange colors of the logo and in fact are experimenting with other colors as we speak.

Please note that what we're looking for is the design for the home page, plus a sub page design.

Target Market(s)

CEOs, corporate social responsibility managers, general managers, business owners, charities, the media

Industry/Entity Type

Communications

Requirements
Must have
• Video on home page
Newsletter sign up on all pages
Navigation as per the attached PDF example

```html
<!DOCTYPE html>
<html lang="en">
<head>
<meta charset="utf-8">
<title>BrightLot – Charity Auctions</title>
<link href="https://fonts.googleapis.com/css2?family=Lato:ital,wght@0,400;0,700;1,700&display=swap" rel="stylesheet">
<style>
  :root {
    --ink: #4a4a4a;
    --ink-soft: #666;
    --brand-blue: #1d3f8a;
    --navy: #16264d;
    --orange: #d98d1e;
    --orange-dark: #b8730f;
    --submit-top: #1a8fd0;
    --submit-bottom: #0a5a9a;
    --panel: #eef1f4;
    --rule: #b5b5b5;
    --icon: #6d6d6d;
  }
  * { box-sizing: border-box; margin: 0; padding: 0; }
  html, body { width: 1200px; height: 707px; overflow: hidden; }
  body {
    font-family: "Lato", sans-serif;
    color: var(--ink);
    position: relative;
    background: #e9e9e9;
  }
  .backdrop {
    position: absolute; inset: 0;
    background:
      radial-gradient(ellipse at 50% 40%, rgba(255,255,255,.85), rgba(255,255,255,.35) 70%),
      linear-gradient(135deg, #d8d8d8, #f0f0f0 40%, #cfcfcf 70%, #e6e6e6);
  }
  .abs { position: absolute; }

  /* header */
  .brand { left: 202px; top: 38px; display: flex; align-items: center; gap: 10px; }
  .brand-dot { width: 44px; height: 44px; border-radius: 50%; background: var(--orange); }
  .brand-name { font-size: 30px; font-weight: 700; color: var(--brand-blue); letter-spacing: -0.5px; }
  .main-nav { left: 485px; top: 54px; display: flex; align-items: center; font-size: 16px; letter-spacing: .5px; color: #333; }
  .main-nav span { padding: 0 14px; }
  .main-nav span:first-child { padding-left: 0; }
  .main-nav span + span { border-left: 1px dotted #999; }
  .social { display: flex; gap: 20px; }
  .social i { display: block; width: 20px; height: 20px; border-radius: 50%; background: var(--icon); }
  .header-social { left: 862px; top: 54px; }
  .header-rule { left: 188px; top: 96px; width: 812px; height: 1px; background: var(--rule); }

  /* side menu */
  .side-menu {
    left: 212px; top: 148px; width: 174px; height: 218px;
    background: linear-gradient(#fafbfc, var(--panel));
    border: 1px solid #d3d6da; border-radius: 3px 0 0 3px;
    box-shadow: 0 2px 6px rgba(0,0,0,.12);
  }
  .side-menu ul { list-style: none; margin-top: 33px; }
  .side-menu li {
    margin-left: 22px; margin-right: 18px; height: 35.5px; line-height: 35px;
    text-align: right; font-size: 13px; color: #333;
    border-top: 1px dotted #bbb;
  }
  .side-home {
    left: 206px; top: 153px; width: 180px; height: 26px;
    background: linear-gradient(90deg, #0f1a33, var(--navy) 40%, #1e3a78);
    clip-path: polygon(0 0, 100% 0, 100% 100%, 0 100%, 5px 50%);
    color: #fff; font-size: 13px; text-align: right; line-height: 26px; padding-right: 18px;
  }

  /* video */
  .video-frame {
    left: 386px; top: 122px; width: 414px; height: 260px;
    background: #55585c; border: 1px solid #3a3c3f;
    box-shadow: 0 3px 8px rgba(0,0,0,.3);
  }
  .video-still {
    left: 394px; top: 130px; width: 398px; height: 244px;
    background: linear-gradient(#3a3a3a, #2a2a2a 45%, #1e1e1e 60%, #2c2c2c);
  }
  .play {
    left: 542px; top: 196px; width: 92px; height: 92px; border-radius: 50%;
    background: radial-gradient(circle at 50% 30%, #cfcfcf, #8a8a8a);
    box-shadow: 0 4px 10px rgba(0,0,0,.5);
  }
  .play-inner {
    left: 550px; top: 204px; width: 76px; height: 76px; border-radius: 50%;
    background: radial-gradient(circle at 50% 25%, #ffffff, #d6d6d6 70%, #bdbdbd);
  }

  /* subscribe */
  .subscribe {
    left: 800px; top: 148px; width: 193px; height: 218px;
    background: linear-gradient(var(--orange), var(--orange-dark));
    border-radius: 0 4px 4px 0; padding: 8px 11px;
    box-shadow: 0 2px 6px rgba(0,0,0,.2); color: #fff;
  }
  .subscribe h2 { font-weight: 400; font-size: 22px; line-height: 1; margin: 2px 0 8px; }
  .subscribe p { font-size: 9.5px; line-height: 12.4px; letter-spacing: -0.1px; }
  .field {
    position: absolute; height: 18px; background: #fff; border: 1px solid #e0b56e;
    color: #aaa; font-size: 9.5px; line-height: 16px; padding-left: 5px;
  }
  .submit {
    position: absolute; left: 11px; top: 180px; width: 171px; height: 26px;
    background: linear-gradient(var(--submit-top), var(--submit-bottom));
    border: 1px solid #0a4a80; color: #fff; font-weight: 700; font-size: 19px;
    text-align: center; line-height: 24px;
  }

  /* quote */
  .quote-mark { color: rgba(120,120,120,.18); font-size: 180px; font-family: Georgia, serif; line-height: 1; }
  .quote {
    left: 268px; top: 427px; width: 700px;
    font-size: 20.3px; line-height: 25px; color: #555;
  }
  .quote-author { left: 268px; top: 537px; font-size: 22px; font-weight: 700; font-style: italic; color: var(--orange); }

  /* footer */
  .footer-rule { left: 192px; top: 598px; width: 812px; height: 1px; background: var(--rule); }
  .footer-rule.dotted { top: 654px; background: none; border-top: 1px dotted #bbb; height: 0; }
  .footer-mark { left: 203px; top: 615px; width: 26px; height: 26px; border-radius: 50%; background: #8a8a8a; }
  .footer-nav { left: 346px; top: 621px; display: flex; gap: 12.5px; font-size: 11px; color: #555; }
  .footer-social { left: 857px; top: 618px; }
  .copyright { left: 0; width: 1200px; top: 666px; text-align: center; font-size: 11px; color: #555; }
</style>
</head>
<body>
  <div class="backdrop" role="img" aria-label="Faded collage of tropical holiday photographs"></div>

  <header>
    <div class="abs brand"><span class="brand-dot"></span><span class="brand-name">BrightLot</span></div>
    <nav class="abs main-nav"><span>DONOR</span><span>CHARITIES</span><span>AUCTIONS</span></nav>
    <div class="abs social header-social"><i></i><i></i><i></i><i></i></div>
    <div class="abs header-rule"></div>
  </header>

  <nav class="abs side-menu">
    <ul>
      <li>How it Works</li>
      <li>Acts of Goodness</li>
      <li>Goodness Partners</li>
      <li>About</li>
      <li>Contact</li>
    </ul>
  </nav>
  <div class="abs side-home">Home</div>

  <div class="abs video-frame"></div>
  <div class="abs video-still" role="img" aria-label="Video still of an overwater beach hut at dusk"></div>
  <div class="abs play"></div>
  <div class="abs play-inner"></div>
  <svg class="abs" style="left:576px;top:231px" width="26" height="24" viewBox="0 0 26 24"><path d="M2 1 L24 12 L2 23 Z" fill="#111"/></svg>

  <section class="abs subscribe">
    <h2>Subscribe</h2>
    <p>Charity auctions are a great way to get luxury items and unique experiences while helping a worthwhile cause. Subscribe to our email list to be kept informed about upcoming auctions.</p>
    <div class="field" style="left:11px;top:108px;width:83px">First Name</div>
    <div class="field" style="left:99px;top:108px;width:83px">Last Name</div>
    <div class="field" style="left:11px;top:132px;width:171px">City / Town</div>
    <div class="field" style="left:11px;top:156px;width:171px">Email Address</div>
    <div class="submit">Submit</div>
  </section>

  <div class="abs quote-mark" style="left:215px;top:380px">“</div>
  <div class="abs quote-mark" style="left:780px;top:460px">”</div>
  <blockquote class="abs quote">In the end, though, maybe we must all give up trying to pay back the people in this world who sustain our lives. In the end, maybe it’s wiser to surrender before the miraculous scope of human generosity and to just keep saying thank you, forever and sincerely, for as long as we have voices.</blockquote>
  <div class="abs quote-author">— Eliza Garnett</div>

  <footer>
    <div class="abs footer-rule"></div>
    <div class="abs footer-mark"></div>
    <nav class="abs footer-nav"><span>Home</span><span>How it Works</span><span>Acts of Goodness</span><span>Goodness Partners</span><span>About</span><span>Contact</span></nav>
    <div class="abs social footer-social"><i></i><i></i><i></i><i></i></div>
    <div class="abs footer-rule dotted"></div>
    <div class="abs copyright">Copyrights © BrightLot. All rights reserved.</div>
  </footer>
</body>
</html>
```